Bref créative
Biz Card for a Professional Organizer
Dana Kowalt
Cutting-Edge
Room Clearing Maestro
Serving the Bay Area
info@42plumova.com
www.42plumova.com
I'd like a clean design, possibly going vertical instead of the traditional horizontal-UNLESS it is just going to look better going horizontal.
I'm open to suggestions here. I also have black and white versions of my logo if that would work well here...
black version of logo
reverse version of logo
color version

```html
<!DOCTYPE html>
<html lang="en">
<head>
<meta charset="utf-8">
<title>42 Plumova – Business Card</title>
<link rel="stylesheet" href="https://fonts.googleapis.com/css2?family=Questrial&display=swap">
<style>
  :root {
    --stage: #3f4143;
    --label: #a9abad;
    --teal-light: #5fb4c8;
    --teal-mid: #2f8aa6;
    --teal-deep: #1b6a8a;
    --card-blue: #1d6d8f;
    --white: #ffffff;
    --ring: #d9dcde;
    --name-teal: #2b7f9d;
  }
  * { margin: 0; padding: 0; box-sizing: border-box; }
  html, body { width: 1200px; height: 871px; overflow: hidden; }
  body {
    background: var(--stage);
    font-family: "Questrial", "Helvetica Neue", Arial, sans-serif;
    position: relative;
  }
  .card {
    position: absolute;
    top: 108px;
    width: 370px;
    height: 650px;
    border-radius: 12px;
    overflow: hidden;
  }
  .card-back {
    left: 139px;
    background: radial-gradient(ellipse 120% 80% at 30% 25%, var(--teal-light) 0%, var(--teal-mid) 45%, var(--teal-deep) 100%);
  }
  .card-front { left: 674px; background: var(--card-blue); }

  .faint-mark {
    position: absolute;
    left: 45px; top: 60px;
    width: 280px; height: 280px;
    border-radius: 50%;
    background: rgba(255,255,255,0.10);
  }
  .brand-name {
    font-size: 44px;
    line-height: 1;
    letter-spacing: 1px;
    white-space: nowrap;
  }
  .back-brand {
    position: absolute;
    left: 0; right: 0; top: 446px;
    text-align: center;
    color: var(--white);
  }
  .back-web {
    position: absolute;
    left: 0; right: 0; top: 602px;
    text-align: center;
    color: var(--white);
    font-size: 16px;
    letter-spacing: 3px;
  }

  .front-shape { position: absolute; inset: 0; }
  .front-brand {
    position: absolute;
    left: 40px; top: 100px;
    color: var(--name-teal);
  }
  .front-brand .brand-name { font-size: 40px; }

  .contact {
    position: absolute;
    left: 84px; top: 402px;
    color: var(--white);
  }
  .person-name { font-size: 24px; line-height: 28px; letter-spacing: 1px; text-transform: uppercase; }
  .person-role { font-size: 15px; line-height: 20px; letter-spacing: 1px; }
  .service { font-size: 20px; line-height: 26px; margin-top: 50px; }
  .contact-lines { margin-top: 10px; font-size: 18px; line-height: 30px; }

  .label {
    position: absolute;
    top: 779px;
    width: 370px;
    text-align: center;
    color: var(--label);
    font-size: 22px;
  }
  .label-back { left: 139px; }
  .label-front { left: 674px; }
</style>
</head>
<body>
  <section class="card card-back">
    <div class="faint-mark"></div>
    <div class="back-brand">
      <div class="brand-name">42 Plumova</div>
    </div>
    <div class="back-web">www.42plumova.com</div>
  </section>

  <section class="card card-front">
    <svg class="front-shape" viewBox="0 0 370 650" width="370" height="650">
      <circle cx="100" cy="-22" r="312" fill="var(--ring)"/>
      <circle cx="94" cy="-26" r="300" fill="var(--white)"/>
    </svg>
    <div class="front-brand">
      <div class="brand-name">42 Plumova</div>
    </div>
    <div class="contact">
      <div class="person-name">Dana Kowalt</div>
      <div class="person-role">Room Clearing Maestro</div>
      <div class="service">Serving the Bay Area</div>
      <div class="contact-lines">
        <div>(510) 555-0142</div>
        <div>info@42plumova.com</div>
        <div>www.42plumova.com</div>
      </div>
    </div>
  </section>

  <div class="label label-back">Back</div>
  <div class="label label-front">Front</div>
</body>
</html>
```